Creative Real Estate Listing Mailer

I would like a creative double sided Real Estate listing flier/mailer to send out enticing people to list their house for sale with me. An example in my head, but feel free to be creative,.. would be one side with a Weiner dog with a sack of money on its back saying something like " its time to cash in" and the other side having some kind of southwest backdrop ( I live in Arizona) or luxury home, with my photo and my contact info saying something like list your house with me, or see what your home is worth etc.

Target Market(s)

People interested in selling their homes

Industry/Entity Type

Real Estate Agent

Contact Information for Business Card

Similar to the flyer, but simpler

Requirements
Must have
• My name: Brent Holloway
My Email: brentholloway@mailvista.net
My Phone# (480) 317 4926
Website www.Brentholloway.com

```html
<!DOCTYPE html>
<html lang="en">
<head>
<meta charset="utf-8">
<title>Listing Mailer – Brent Holloway</title>
<link rel="stylesheet" href="https://fonts.googleapis.com/css2?family=PT+Sans:wght@400;700&family=PT+Sans+Narrow:wght@700&family=Yellowtail&display=swap">
<style>
  :root {
    --page-bg: #e9e9e9;
    --navy: #1d367f;
    --royal: #3a5aae;
    --royal-light: #4f6fc0;
    --ink: #222;
    --heading-blue: #3853a6;
    --signature-red: #c1272d;
    --rule-grey: #c4c4c4;
    --card-white: #ffffff;
  }
  * { box-sizing: border-box; margin: 0; padding: 0; }
  html, body { width: 1095px; height: 1200px; overflow: hidden; }
  body { background: var(--page-bg); font-family: "PT Sans", Arial, sans-serif; position: relative; }

  .mailer-side {
    position: absolute; left: 77px;
    width: 703px; height: 402px;
    transform: scale(1.3371); transform-origin: 0 0;
    background: var(--card-white); overflow: hidden;
    box-shadow: 0 2px 6px rgba(0,0,0,.18);
  }
  .mailer-front { top: 42px; }
  .mailer-back { top: 621px; }
  .side-art { position: absolute; inset: 0; width: 703px; height: 402px; }

  /* front */
  .headline {
    position: absolute; left: 24px; top: 28px;
    font-family: "PT Sans Narrow", "Arial Narrow", sans-serif; font-weight: 700;
    font-size: 54px; line-height: 54px; color: #fff;
    text-shadow: 0 2px 4px rgba(0,0,0,.55); letter-spacing: -0.5px;
  }
  .offer-panel { position: absolute; left: 32px; top: 226px; color: #fff; }
  .offer-question { font-weight: 700; font-size: 27px; line-height: 36px; }
  .offer-rule { width: 138px; height: 2px; background: #fff; margin: 10px 0 10px; }
  .offer-detail { font-size: 19px; line-height: 25px; }
  .offer-agent { font-family: "Yellowtail", cursive; font-size: 17px; color: #c9d3ee; margin-top: 2px; }

  .brand-mark { position: absolute; display: flex; align-items: center; gap: 8px; }
  .brand-square { background: var(--navy); }
  .brand-name { font-weight: 700; color: var(--ink); text-transform: uppercase; letter-spacing: 1.5px; line-height: 1.05; }
  .brand-front { left: 410px; top: 296px; }
  .brand-front .brand-square { width: 42px; height: 42px; }
  .brand-front .brand-name { font-size: 19px; }
  .brand-back { left: 432px; top: 42px; gap: 5px; }
  .brand-back .brand-square { width: 20px; height: 20px; }
  .brand-back .brand-name { font-size: 9.5px; letter-spacing: 1px; }

  /* back */
  .listing-pitch {
    position: absolute; left: 168px; top: 212px;
    font-family: "PT Sans Narrow", "Arial Narrow", sans-serif; font-weight: 700;
    font-size: 22px; line-height: 24px; color: var(--heading-blue);
  }
  .agent-name { position: absolute; left: 168px; top: 292px; font-family: "Yellowtail", cursive; font-size: 24px; color: var(--signature-red); }
  .contact-list { position: absolute; left: 170px; top: 322px; list-style: none; font-size: 13px; line-height: 18px; color: var(--heading-blue); }
  .contact-list li { display: flex; align-items: center; gap: 6px; }
  .contact-list svg { width: 12px; height: 12px; }
  .badge-row { position: absolute; left: 168px; top: 378px; display: flex; align-items: flex-end; gap: 8px; }
  .badge-listing { width: 70px; height: 30px; border: 2px solid var(--navy); }
  .badge-housing { width: 30px; height: 32px; background: var(--ink); }
  .website-band { position: absolute; left: 0; top: 430px; width: 370px; text-align: center; color: #fff; }
  .website-note { font-family: "PT Sans Narrow", "Arial Narrow", sans-serif; font-weight: 700; font-size: 17px; line-height: 22px; }
  .website-url { font-weight: 700; font-size: 16px; line-height: 26px; display: flex; justify-content: center; align-items: center; gap: 8px; }
  .website-url svg { width: 16px; height: 16px; }
</style>
</head>
<body>

<section class="mailer-side mailer-front">
  <svg class="side-art" viewBox="0 0 703 402">
    <defs>
      <linearGradient id="money-scene" x1="0" y1="0" x2="1" y2="0">
        <stop offset="0" stop-color="#4c5548"/>
        <stop offset=".5" stop-color="#8e9580"/>
        <stop offset=".8" stop-color="#b07a44"/>
        <stop offset="1" stop-color="#a69a7c"/>
      </linearGradient>
      <linearGradient id="panel-navy" x1="0" y1="0" x2="1" y2="1">
        <stop offset="0" stop-color="#1a3280"/>
        <stop offset="1" stop-color="#3656a8"/>
      </linearGradient>
      <linearGradient id="paper" x1="0" y1="0" x2="0" y2="1">
        <stop offset="0" stop-color="#ffffff"/>
        <stop offset="1" stop-color="#e6e6e6"/>
      </linearGradient>
    </defs>
    <rect x="0" y="0" width="703" height="300" fill="url(#money-scene)" role="img" aria-label="Photo of a happy dachshund lying on a pile of dollar bills"/>
    <path d="M0,205 C90,165 260,160 370,200 C470,238 560,262 703,238 V402 H0 Z" fill="var(--royal)"/>
    <path d="M372,228 C460,262 570,286 703,258 V402 H356 C380,340 385,280 372,228 Z" fill="url(#paper)"/>
    <path d="M0,222 C90,182 250,178 346,214 C388,232 384,330 338,402 H0 Z" fill="url(#panel-navy)"/>
  </svg>

  <h1 class="headline">ITS TIME<br>TO CASH IN!!!</h1>

  <div class="offer-panel">
    <p class="offer-question">THINKING<br>ABOUT SELING?</p>
    <div class="offer-rule"></div>
    <p class="offer-detail">Special Offer for Arizona<br>Homeowners</p>
    <p class="offer-agent">with: Brent Holloway</p>
  </div>

  <div class="brand-mark brand-front">
    <span class="brand-square"></span>
    <span class="brand-name">Desert Crest<br>Properties</span>
  </div>
</section>

<section class="mailer-side mailer-back">
  <svg class="side-art" viewBox="0 0 703 402" preserveAspectRatio="none" style="height:500px" >
  </svg>
  <svg class="side-art" viewBox="0 0 703 500" style="height:500px; top:-0px">
    <defs>
      <linearGradient id="home-scene" x1="0" y1="0" x2="0" y2="1">
        <stop offset="0" stop-color="#b9c2c9"/>
        <stop offset=".55" stop-color="#8a7d6e"/>
        <stop offset=".8" stop-color="#4aa3c8"/>
        <stop offset="1" stop-color="#9a958c"/>
      </linearGradient>
      <linearGradient id="portrait-area" x1="0" y1="0" x2="0" y2="1">
        <stop offset="0" stop-color="#d9d9d9"/>
        <stop offset=".4" stop-color="#bfbfbf"/>
        <stop offset="1" stop-color="#1f2a44"/>
      </linearGradient>
      <linearGradient id="band-navy" x1="0" y1="0" x2="1" y2="0">
        <stop offset="0" stop-color="#1a2d66"/>
        <stop offset="1" stop-color="#0f1f4e"/>
      </linearGradient>
      <linearGradient id="pitch-bg" x1="0" y1="0" x2="1" y2="0">
        <stop offset="0" stop-color="#e4e4e4"/>
        <stop offset="1" stop-color="#ffffff"/>
      </linearGradient>
    </defs>
    <rect x="0" y="198" width="400" height="230" fill="url(#pitch-bg)"/>
    <rect x="0" y="0" width="380" height="182" fill="url(#home-scene)" role="img" aria-label="Photo of a modern luxury home with a pool at dusk"/>
    <rect x="0" y="185" width="155" height="240" fill="url(#portrait-area)" role="img" aria-label="Portrait photo of the agent in a dark suit"/>
    <path d="M0,425 H392 C380,455 362,480 340,500 H0 Z" fill="url(#band-navy)"/>
    <path d="M400,0 C380,100 410,230 430,380 C434,430 428,470 426,500 H418 C420,470 426,430 422,380 C404,230 372,100 392,0 Z" fill="#e2e2e2"/>
    <path d="M362,0 H394 C374,100 404,230 424,380 C428,430 424,470 420,500 H338 C372,470 396,430 400,380 C384,230 344,110 362,0 Z" fill="var(--royal)"/>
    <rect x="597" y="27" width="85" height="75" fill="none" stroke="var(--rule-grey)" stroke-width="1.5"/>
    <g stroke="var(--rule-grey)" stroke-width="1.2">
      <line x1="412" y1="183" x2="682" y2="183"/>
      <line x1="412" y1="232" x2="682" y2="232"/>
      <line x1="412" y1="282" x2="682" y2="282"/>
      <line x1="412" y1="331" x2="682" y2="331"/>
    </g>
  </svg>

  <div class="brand-mark brand-back">
    <span class="brand-square"></span>
    <span class="brand-name">Desert Crest<br>Properties</span>
  </div>

  <h2 class="listing-pitch">LIST YOUR<br>HOUSE FOR SALE<br>WITH ME</h2>
  <p class="agent-name">Brent Holloway</p>
  <ul class="contact-list">
    <li>
      <svg viewBox="0 0 12 12"><circle cx="6" cy="6" r="5.3" fill="none" stroke="currentColor" stroke-width="1"/><path d="M4,3.2 L5,3 5.6,4.6 4.9,5.1 C5.3,6 6,6.7 6.9,7.1 L7.4,6.4 9,7 8.8,8 C6.2,8.3 3.7,5.8 4,3.2 Z" fill="currentColor"/></svg>
      (480) 317 4926
    </li>
    <li>
      <svg viewBox="0 0 12 12"><circle cx="6" cy="6" r="5.6" fill="currentColor"/><rect x="3" y="4" width="6" height="4" fill="none" stroke="#fff" stroke-width=".9"/><path d="M3,4 L6,6.3 9,4" fill="none" stroke="#fff" stroke-width=".9"/></svg>
      brentholloway@mailvista.net
    </li>
  </ul>
  <div class="badge-row">
    <span class="badge-listing"></span>
    <span class="badge-housing"></span>
  </div>

  <div class="website-band" style="top:443px">
    <p class="website-note">VISIT OUR WEBSITE FOR MORE INFORMATION</p>
    <p class="website-url">
      <svg viewBox="0 0 16 16"><circle cx="8" cy="8" r="7" fill="none" stroke="#fff" stroke-width="1.5"/><ellipse cx="8" cy="8" rx="3" ry="7" fill="none" stroke="#fff" stroke-width="1.2"/><line x1="1" y1="8" x2="15" y2="8" stroke="#fff" stroke-width="1.2"/></svg>
      www.Brentholloway.com
    </p>
  </div>
</section>

<style>
  .mailer-back { height: 500px; transform: scale(1.3371, 1.0750); }
  .mailer-back > svg:first-child { display: none; }
</style>
</body>
</html>
```